Norvale Works - pioneers of next generation consulting!

We are a next generation management consulting firm with two focus areas and USPs (unique selling points):>Technology driven business developmentWe are not developers, we are experts in HOW to apply and incorporate technology in your business dna to drive business growth and value-added change.>Creating high performing teams levering our philosophy of collective intelligence. We truly understand the need of human engagement and we know that the only way of getting there is by building strong relationships among people, a warm and open culture is a stepping stone towards effective collaboration within/among teams. - We don't want a ”corporate feel” to our templates. The organic feeling we have with our blue-on-blue blobs has the idea of ever changing movement and shape changing. Please see our website, www.norvaleworks.se. - In our context we sit among classic business mgmt. consultants and classic IT mgmt. consultants. We cater to business, tech and humans as the ultimate vehicle of change and business value. -To have a clean template one suggestion is to only use blue, white and black and keeping other colors separate, as an alternative but we are truly open allow your creativity add value to this. We are looking to find a slide deck which we can pick slides from, depending on what/whom/why we interact with customer we want to create different outcomes and our presentations should support this.

Industry/Entity Type

Management Consulting

Requirements
Must have
• next generation powerpoint and how to package storytelling. please keep to our look and feel, we just arrived at our logo, colours and shapes. Help us to carry it into our ppt's as well.
Should not have
• Hi all, please have a look at our website. It is still very new and more will be done, but our goal is to make powerpoint to come alive again and mirror our pioneering hearts and brains.

```html
<!DOCTYPE html>
<html lang="en">
<head>
<meta charset="utf-8">
<title>Norvale Works – Slide Deck Overview</title>
<link rel="stylesheet" href="https://fonts.googleapis.com/css2?family=Open+Sans:wght@400;600;700&display=swap">
<style>
  :root{
    --stage:#91a8c1;
    --blue:#2f6fd8;
    --blue-mid:#3d7ee6;
    --blue-soft:#6d9cec;
    --blue-deep:#1f4ea3;
    --navy:#1d3d86;
    --pale:#e4ecf9;
    --pale-2:#d3e0f6;
    --ink:#1c1c1c;
    --muted:#6b7788;
    --white:#ffffff;
    --teal:#8fd3d6;
    --coral:#e25563;
  }
  *{box-sizing:border-box;margin:0;padding:0}
  html,body{width:1136px;height:1200px;overflow:hidden}
  body{background:var(--stage);font-family:'Open Sans',sans-serif;color:var(--ink)}
  .board{position:relative;width:1136px;height:1200px}

  .slide{position:absolute;width:293px;height:184px;background:var(--white);overflow:hidden;box-shadow:0 2px 7px rgba(28,48,80,.28)}
  .slide.is-blue{background:var(--blue)}
  .col-1{left:116px}.col-2{left:421px}.col-3{left:725px}
  .row-1{top:19px}.row-2{top:214px}.row-3{top:409px}.row-4{top:604px}.row-5{top:800px}.row-6{top:996px}

  .shape{position:absolute;inset:0;width:100%;height:100%}
  .el{position:absolute}
  .art{position:absolute;border-radius:22px;background:linear-gradient(140deg,#eaf1fc,#9fbdf0 60%,#4f84df)}
  .art.on-blue{background:linear-gradient(140deg,#a9c6f5,#5b8fe6 55%,#2a5fc4)}
  .photo{position:absolute;background:linear-gradient(135deg,#5d7fa8,#2c4468)}

  .brand{position:absolute;font-weight:700;text-transform:uppercase;color:var(--navy);letter-spacing:.05em;line-height:1.05}
  .brand.lg{font-size:8px}
  .brand.sm{font-size:4.2px;right:10px;top:9px;text-align:left}
  .brand.white{color:var(--white)}

  .hero-title{position:absolute;left:19px;top:55px;font-size:17.5px;font-weight:400;line-height:1.13;color:var(--ink)}
  .hero-lead{position:absolute;left:21px;top:100px;width:150px;font-size:6.8px;line-height:1.4;color:var(--blue)}
  .hero-meta{position:absolute;left:21px;top:138px;font-size:4.6px;line-height:1.5;color:#444}
  .hero-meta b{font-weight:700}
  .hero-meta .gap{display:block;height:8px}
  .hero-meta .url{font-weight:700;color:var(--blue)}
  .is-blue .hero-title,.is-blue .hero-lead,.is-blue .hero-meta,.is-blue .hero-meta .url{color:var(--white)}

  .slide-title{position:absolute;left:18px;top:20px;font-size:9px;font-weight:600;color:var(--ink)}
  .title-dot{position:absolute;left:6px;top:26px;width:11px;height:11px;border-radius:50%;background:var(--blue-soft)}
  .foot{position:absolute;left:9px;bottom:7px;font-size:3.6px;color:#8b97a8}
  .page-no{position:absolute;right:-4px;bottom:-4px;width:20px;height:20px;border-radius:50%;background:var(--blue-soft);color:var(--white);font-size:3.8px;padding:5px 0 0 6px}
  .tiny{font-size:3.8px;line-height:1.45;color:#444}

  /* slide 4 */
  .statement{position:absolute;left:97px;top:43px;font-size:14.5px;line-height:1.12;color:var(--white);font-weight:400}
  .case{position:absolute;left:95px;top:101px;width:40px;height:58px;background:var(--navy);padding:4px;font-size:2.8px;line-height:1.35;color:var(--white)}
  .case b{display:block;font-weight:700;margin-top:2px}
  .caption{position:absolute;font-size:2.6px;color:var(--white)}

  /* divider */
  .divider-title{position:absolute;left:47px;top:86px;font-size:15.5px;font-weight:700;color:var(--blue)}
  .divider-sub{position:absolute;left:49px;top:105px;font-size:4px;color:#444}

  /* agenda */
  .agenda-title{position:absolute;left:104px;top:27px;font-size:12px;color:var(--ink)}
  .agenda-intro{position:absolute;left:104px;top:43px;width:160px;font-size:3.6px;line-height:1.4;color:#444}
  .agenda-list{position:absolute;list-style:none;font-size:5px;color:var(--blue)}
  .agenda-list li{height:22px;display:flex;align-items:flex-start;gap:7px}
  .agenda-list .num{width:8px;height:8px;border-radius:50%;background:var(--blue);color:var(--white);font-size:3.6px;display:flex;align-items:center;justify-content:center;margin-top:-1px}

  /* intro */
  .intro-lead{position:absolute;left:36px;top:49px;width:112px;font-size:6.8px;line-height:1.45;color:#333}
  .intro-lead .name{color:var(--blue);font-weight:600}
  .intro-body{position:absolute;left:36px;top:106px;width:108px}

  /* three columns */
  .center-title{position:absolute;left:0;right:0;top:16px;text-align:center;font-size:8px;font-weight:600;color:var(--white)}
  .center-sub{position:absolute;left:46px;width:200px;top:32px;text-align:center;font-size:5.4px;line-height:1.4;color:var(--white)}
  .col-box{position:absolute;top:57px;width:74px;height:96px;background:var(--blue-deep);border-radius:3px;padding:40px 5px 0;color:var(--white)}
  .col-box h4{font-size:4.4px;font-weight:700;margin-bottom:2px}
  .col-box p{font-size:3.6px;line-height:1.4;text-align:justify}
  .col-box .icon{position:absolute;left:28px;top:14px;width:18px;height:18px}

  /* image with text */
  .iwt-title{position:absolute;left:20px;top:20px;font-size:8px;font-weight:600;color:var(--white)}
  .iwt-lead{position:absolute;left:22px;top:35px;width:120px;font-size:5.6px;line-height:1.35;color:var(--white)}
  .iwt-body{position:absolute;left:22px;top:64px;width:126px;font-size:3.6px;line-height:1.45;color:#e6eefc}

  /* custom bar */
  .bar-lead{position:absolute;left:154px;top:46px;width:122px;font-size:6.4px;line-height:1.4;color:#333}
  .stat{position:absolute;left:154px;display:flex;gap:3px;width:125px}
  .stat .pct{font-size:9px;font-weight:400;line-height:1}
  .stat p{font-size:3.5px;line-height:1.4;color:#444}

  /* six categories */
  .cat{position:absolute;width:83px;height:58px;background:var(--blue);border:1px solid #5f95ea;border-radius:3px;padding:26px 5px 0;color:var(--white)}
  .cat h4{font-size:3.8px;font-weight:700;border-bottom:.5px solid rgba(255,255,255,.6);padding-bottom:1px;margin-bottom:1px}
  .cat p{font-size:3.6px;line-height:1.4}
  .cat .icon{position:absolute;left:6px;top:6px;width:14px;height:14px}

  /* statistic */
  .stat-note{position:absolute;left:157px;top:55px;width:88px;font-size:3.6px;line-height:1.4;color:#333}
  .stat-note b{display:block;font-weight:700;margin-bottom:3px}
  .stat-note ul{padding-left:6px}
  .stat-note li{margin-bottom:2px}

  /* timeline */
  .tl-entry{position:absolute;width:70px;font-size:3.6px;line-height:1.35;color:#333}
  .tl-entry b{display:block;font-size:3.8px;font-weight:700;margin-bottom:3px}

  /* testimonial */
  .quote-box{position:absolute;width:85px;height:32px;background:var(--blue-deep);border:1px solid #6a9be9;border-radius:2px;padding:4px 6px;font-size:3.4px;line-height:1.4;color:var(--white)}
  .quote-frame{position:absolute;width:35px;height:32px;border:1px solid #6a9be9;border-radius:2px;background:var(--white)}
  .quote-name{position:absolute;font-size:4.6px;font-weight:600;color:#222;line-height:1.2}
  .quote-name span{display:block;font-size:2.8px;font-weight:400;color:#777}

  /* thank you */
  .thanks{position:absolute;font-size:13px;font-weight:600;color:var(--blue)}
  .contact{position:absolute;font-size:4.8px;line-height:1.45;color:#333}
  .is-blue .thanks,.is-blue .contact{color:var(--white)}
  .follow{position:absolute;font-size:4.6px;font-weight:600;color:var(--blue)}
  .is-blue .follow{color:var(--white)}

  /* disclaimer */
  .legal{position:absolute;left:18px;top:41px;width:261px;font-size:3.6px;line-height:1.5;color:#444;text-align:justify}
  .legal p{margin-bottom:3px}

  /* quote */
  .quote-text{position:absolute;left:58px;top:73px;width:115px;font-size:6.4px;line-height:1.4;color:#333}
  .quote-author{position:absolute;left:58px;top:129px;font-size:6px;font-weight:700;color:#222}
</style>
</head>
<body>
<main class="board">

  <!-- Row 1: title slides -->
  <section class="slide col-1 row-1">
    <svg class="shape" viewBox="0 0 293 184" aria-hidden="true"><path d="M168 0H293V128C276 150 252 128 236 150C216 178 182 176 170 150C158 124 196 100 182 72C168 44 148 22 168 0Z" fill="var(--blue)"/></svg>
    <div class="art" role="img" aria-label="Isometric illustration of a person working on a large laptop with bar charts" style="left:150px;top:30px;width:138px;height:130px"></div>
    <div class="brand lg" style="left:22px;top:14px">Norvale<br>Works</div>
    <h1 class="hero-title">Technology<br>Development</h1>
    <p class="hero-lead">Managing your Technology Development extremely quick by lorem ipsum.</p>
    <p class="hero-meta">Author Name<br><b>Business Division Name</b><span class="gap"></span>18 April 2019<br><span class="url">www.norvaleworks.se</span></p>
  </section>

  <section class="slide col-2 row-1 is-blue">
    <svg class="shape" viewBox="0 0 293 184" aria-hidden="true"><path d="M175 0H293V184H200C176 160 214 140 196 112C178 86 150 76 166 46C174 28 182 14 175 0Z" fill="var(--blue-mid)"/></svg>
    <div class="art on-blue" role="img" aria-label="Isometric illustration of a person working on a large laptop with bar charts" style="left:150px;top:30px;width:138px;height:130px"></div>
    <div class="brand lg white" style="left:22px;top:14px">Norvale<br>Works</div>
    <h1 class="hero-title">Technology<br>Development</h1>
    <p class="hero-lead">Managing your Technology Development extremely quick by lorem ipsum.</p>
    <p class="hero-meta">Author Name<br><b>Business Division Name</b><span class="gap"></span>18 April 2019<br><span class="url">www.norvaleworks.se</span></p>
  </section>

  <section class="slide col-3 row-1">
    <svg class="shape" viewBox="0 0 293 184" aria-hidden="true"><path d="M0 150C20 140 40 160 38 184H0Z" fill="var(--pale-2)"/><path d="M293 110C270 120 262 150 275 184H293Z" fill="var(--pale)"/></svg>
    <div class="art" role="img" aria-label="Isometric illustration of a person working on a large laptop with bar charts" style="left:150px;top:30px;width:138px;height:130px"></div>
    <div class="brand lg" style="left:22px;top:14px">Norvale<br>Works</div>
    <div class="el" style="right:12px;top:11px;font-size:4.4px;font-weight:700;color:var(--blue)">www.norvaleworks.se</div>
    <h1 class="hero-title">Technology<br>Development</h1>
    <p class="hero-lead">Managing your Technology Development extremely quick by lorem ipsum.</p>
    <p class="hero-meta">Author Name<br><b>Business Division Name</b><span class="gap"></span>18 April 2019</p>
  </section>

  <!-- Row 2 -->
  <section class="slide col-1 row-2 is-blue">
    <svg class="shape" viewBox="0 0 293 184" aria-hidden="true"><path d="M30 0H160C185 20 240 10 262 40C290 80 250 110 210 118C160 128 120 150 80 166C50 178 20 160 22 120C24 80 0 40 30 0Z" fill="var(--blue-deep)"/></svg>
    <p class="statement">we make your company flexible enough for future challenge</p>
    <div class="photo" role="img" aria-label="Photo of a consultant in a purple shirt working at a lab station" style="left:12px;top:100px;width:84px;height:60px"></div>
    <div class="case">CASE STUDY<br>NORDMARK<b>PROBLEM</b>Culture gaps in a firm with roots in the 60s<b>RESULTS</b>Faster decisions at all levels</div>
    <div class="photo" role="img" aria-label="Photo of a team workshop around a table" style="left:146px;top:101px;width:40px;height:28px"></div>
    <div class="caption" style="left:146px;top:132px">Workshop – Active coaching methods</div>
    <div class="caption" style="left:13px;top:164px">INSIGHT | Future challenge demands a flexible organisation</div>
  </section>

  <section class="slide col-2 row-2">
    <svg class="shape" viewBox="0 0 293 184" aria-hidden="true"><path d="M293 60C262 70 240 58 210 76C176 96 150 130 156 160C160 178 170 184 176 184H293Z" fill="var(--blue)"/><path d="M293 110C270 120 250 110 232 132C218 150 220 172 232 184H293Z" fill="var(--blue-mid)"/></svg>
    <div class="art" role="img" aria-label="Illustration of a person carrying a large rocket" style="left:130px;top:30px;width:105px;height:130px"></div>
    <svg class="el" style="left:30px;top:87px;width:14px;height:14px" viewBox="0 0 14 14" aria-hidden="true"><path d="M3 11L6 8M5 10C6 6 9 3 12 2C11 5 8 8 4 9Z" fill="none" stroke="var(--blue)" stroke-width="1.1" stroke-linejoin="round"/></svg>
    <h2 class="divider-title">divider title</h2>
    <p class="divider-sub">place a subtitle / desc here</p>
  </section>

  <section class="slide col-3 row-2">
    <svg class="shape" viewBox="0 0 293 184" aria-hidden="true"><path d="M0 30C20 20 44 40 52 70C60 100 86 120 84 150C82 172 70 184 60 184H0Z" fill="var(--blue)"/></svg>
    <div class="art" role="img" aria-label="Illustration of a woman standing and waving" style="left:22px;top:32px;width:50px;height:148px;border-radius:20px"></div>
    <h2 class="agenda-title">Presentation Agenda</h2>
    <p class="agenda-intro">Temporibus autem quibusdam et aut officiis debitis aut rerum necessitatibus. Quis autem voluptate velit esse quam nihil molestiae.</p>
    <ol class="agenda-list" style="left:104px;top:68px">
      <li><span class="num">1</span>Introduction</li>
      <li><span class="num">2</span>The Company</li>
      <li><span class="num">3</span>The Business Value</li>
      <li><span class="num">4</span>The Private Equity</li>
    </ol>
    <ol class="agenda-list" style="left:201px;top:68px">
      <li><span class="num">5</span>Why Choose Us</li>
      <li><span class="num">6</span>Our Clients</li>
      <li><span class="num">7</span>Lorem Ipsum</li>
      <li><span class="num">8</span>Contact Us</li>
    </ol>
  </section>

  <!-- Row 3 -->
  <section class="slide col-1 row-3">
    <span class="title-dot"></span>
    <h2 class="slide-title">Introduction</h2>
    <div class="brand sm">Norvale<br>Works</div>
    <p class="intro-lead"><span class="name">Norvale Works</span> is a management consulting firm powered by Collective Intelligence.<br>We are a value Driven Company with great passion in people and technology.</p>
    <p class="intro-body tiny">Lorem ipsum dolor sit amet, consectetur adipiscing elit, sed do eiusmod tempor incididunt ut labore et dolore magna aliqua. Ut enim ad minim veniam, quis nostrud exercitation ullamco laboris nisi ut aliquip ex ea commodo consequat. Duis aute dolor inreprehenderit.</p>
    <svg class="shape" viewBox="0 0 293 184" aria-hidden="true"><path d="M186 50C210 36 250 40 270 60C290 80 282 110 262 124C240 140 206 130 190 110C176 92 168 62 186 50Z" fill="var(--blue-soft)"/></svg>
    <div class="art" role="img" aria-label="Illustration of two people working beside a large smartphone showing charts" style="left:160px;top:36px;width:125px;height:126px;background:linear-gradient(140deg,#eaf1fc00,#9fbdf0aa 50%,#4f84dfcc)"></div>
    <p class="foot">Presentation Title goes here | www.norvaleworks.se</p>
    <span class="page-no">01</span>
  </section>

  <section class="slide col-2 row-3">
    <svg class="shape" viewBox="0 0 293 184" aria-hidden="true"><path d="M0 0H293V150C250 160 200 140 146 150C90 160 40 140 0 150Z" fill="var(--blue)"/></svg>
    <div class="brand sm white">Norvale<br>Works</div>
    <h2 class="center-title">Three Column Items</h2>
    <p class="center-sub">Duis aute dolor inreprehenderit. Commodo consequat. Duis aute irure dolor in reprehenderit in voluptate.</p>
    <div class="col-box" style="left:19px"><h4>LOREM IPSUM</h4><p>Lorem ipsum dolor sit amet, consectetur adipiscing elit, sed do eiusmod tempor incididunt ut labore et dolore magna aliqua. Ut enim ad minim veniam, quis nostrud exercitation ullamco</p></div>
    <div class="col-box" style="left:110px">
      <svg class="icon" viewBox="0 0 18 18" aria-hidden="true"><path d="M3 13H8L12 11M9 8V4M9 6C7 6 6 5 6 3M9 5C11 5 12 4 12 2" fill="none" stroke="#fff" stroke-width=".9" stroke-linecap="round"/></svg>
      <h4>LOREM IPSUM</h4><p>Lorem ipsum dolor sit amet, consectetur adipiscing elit, sed do eiusmod tempor incididunt ut labore et dolore magna aliqua. Ut enim ad minim veniam, quis nostrud exercitation ullamco</p></div>
    <div class="col-box" style="left:200px"><h4>LOREM IPSUM</h4><p>Lorem ipsum dolor sit amet, consectetur adipiscing elit, sed do eiusmod tempor incididunt ut labore et dolore magna aliqua. Ut enim ad minim veniam, quis nostrud exercitation ullamco laboris nisi ut aliquip ex ea</p></div>
    <p class="foot">Presentation Title goes here | www.norvaleworks.se</p>
    <span class="page-no">02</span>
  </section>

  <section class="slide col-3 row-3">
    <svg class="shape" viewBox="0 0 293 184" aria-hidden="true"><path d="M0 0H200C230 10 260 14 280 40C296 70 290 120 270 140C240 166 180 150 120 160C70 168 30 170 0 160Z" fill="var(--blue-deep)"/></svg>
    <div class="brand sm white">Norvale<br>Works</div>
    <h2 class="iwt-title">Image with Text</h2>
    <p class="iwt-lead">Duis aute dolor inreprehenderit. Commodo consequat. Duis aute irure dolor in reprehenderit in voluptate.</p>
    <p class="iwt-body">Lorem ipsum dolor sit amet, consectetur adipiscing elit, sed do eiusmod tempor incididunt ut labore et dolore magna aliqua. Ut enim ad minim veniam, quis nostrud exercitation ullamco laboris nisi ut aliquip ex ea commodo consequat. Duis aute dolor inreprehenderit. Commodo consequat. Duis aute irure dolor in reprehenderit in voluptate velit esse cillum dolore eu fugiat nulla pariatur. Excepteur sint occaecat cupidatat non proident, sunt in culpa qui officia deserunt mollit.</p>
    <div class="photo" role="img" aria-label="Photo of hands touching a glowing digital network interface" style="left:140px;top:38px;width:142px;height:116px;border-radius:50%;background:radial-gradient(circle at 45% 45%,#9cc3f0,#3a6fb8 55%,#173a74)"></div>
    <p class="foot" style="color:#c8d6f1">Presentation Title goes here | www.norvaleworks.se</p>
    <span class="page-no">03</span>
  </section>

  <!-- Row 4 -->
  <section class="slide col-1 row-4">
    <span class="title-dot"></span>
    <h2 class="slide-title">Custom Bar Slide</h2>
    <div class="brand sm">Norvale<br>Works</div>
    <svg class="el" style="left:22px;top:38px;width:110px;height:110px" viewBox="0 0 110 110" aria-label="Donut chart split 50, 25 and 25 percent" role="img">
      <circle cx="55" cy="55" r="38" fill="none" stroke="var(--navy)" stroke-width="18" stroke-dasharray="119.4 238.8" transform="rotate(90 55 55)"/>
      <circle cx="55" cy="55" r="38" fill="none" stroke="var(--teal)" stroke-width="18" stroke-dasharray="59.7 238.8" transform="rotate(-90 55 55)"/>
      <circle cx="55" cy="55" r="38" fill="none" stroke="var(--coral)" stroke-width="18" stroke-dasharray="59.7 238.8"/>
      <circle cx="86" cy="30" r="6" fill="#fff" opacity=".35"/><text x="86" y="31.5" font-size="3.6" fill="#fff" text-anchor="middle">45%</text>
      <circle cx="88" cy="78" r="6" fill="#fff" opacity=".35"/><text x="88" y="79.5" font-size="3.6" fill="#fff" text-anchor="middle">35%</text>
      <circle cx="26" cy="90" r="6" fill="#fff" opacity=".35"/><text x="26" y="91.5" font-size="3.6" fill="#fff" text-anchor="middle">60%</text>
    </svg>
    <div class="art" role="img" aria-label="Illustration of two people carrying a large envelope" style="left:58px;top:74px;width:38px;height:38px;border-radius:50%"></div>
    <p class="bar-lead">Technology drives marketplace differentiation today, both running and growing your business.</p>
    <div class="stat" style="top:82px"><span class="pct" style="color:var(--navy)">32%</span><p>Lorem ipsum dolor sit amet, consectetur adipiscing elit, sed do eiusmod tempor incididunt ut labore et dolore.</p></div>
    <div class="stat" style="top:105px"><span class="pct" style="color:var(--coral)">13%</span><p>Ut enim ad minim veniam, quis nostrud exercitation ullamco laboris nisi ut aliquip ex ea commodo consequat. Duis aute dolor inreprehenderit.</p></div>
    <div class="stat" style="top:134px"><span class="pct" style="color:#56b9bd">23%</span><p>Commodo consequat. Duis aute irure dolor in reprehenderit in voluptate velit esse cillum.</p></div>
    <p class="foot">Presentation Title goes here | www.norvaleworks.se</p>
    <span class="page-no">04</span>
  </section>

  <section class="slide col-2 row-4">
    <span class="title-dot"></span>
    <h2 class="slide-title">Six Categories</h2>
    <div class="brand sm">Norvale<br>Works</div>
    <div class="cat" style="left:19px;top:35px"><svg class="icon" viewBox="0 0 14 14" aria-hidden="true"><circle cx="7" cy="6" r="4" fill="none" stroke="#fff" stroke-width=".9"/><path d="M5 12H9" stroke="#fff" stroke-width=".9"/></svg><h4>Lorem Ipsum</h4><p>Lorem Ipsum has been the dummy text and can be replaced with your original text here.</p></div>
    <div class="cat" style="left:108px;top:35px"><svg class="icon" viewBox="0 0 14 14" aria-hidden="true"><path d="M2 7L7 3L12 7V12H2Z" fill="none" stroke="#fff" stroke-width=".9"/></svg><h4>Lorem Ipsum</h4><p>Lorem Ipsum has been the dummy text and can be replaced with your original text here.</p></div>
    <div class="cat" style="left:197px;top:35px"><svg class="icon" viewBox="0 0 14 14" aria-hidden="true"><circle cx="7" cy="7" r="5" fill="none" stroke="#fff" stroke-width=".9"/><path d="M7 2V12M2 7H12" stroke="#fff" stroke-width=".7"/></svg><h4>Lorem Ipsum</h4><p>Lorem Ipsum has been the dummy text and can be replaced with your original text here.</p></div>
    <div class="cat" style="left:19px;top:98px"><svg class="icon" viewBox="0 0 14 14" aria-hidden="true"><path d="M2 12H12M4 11V7M7 11V4M10 11V6" fill="none" stroke="#fff" stroke-width=".9"/></svg><h4>Lorem Ipsum</h4><p>Lorem Ipsum has been the dummy text and can be replaced with your original text here.</p></div>
    <div class="cat" style="left:108px;top:98px"><svg class="icon" viewBox="0 0 14 14" aria-hidden="true"><path d="M2 8L5 5L8 8L11 5L12 6" fill="none" stroke="#fff" stroke-width=".9"/></svg><h4>Lorem Ipsum</h4><p>Lorem Ipsum has been the dummy text and can be replaced with your original text here.</p></div>
    <div class="cat" style="left:197px;top:98px"><svg class="icon" viewBox="0 0 14 14" aria-hidden="true"><rect x="3" y="2" width="8" height="10" fill="none" stroke="#fff" stroke-width=".9"/><path d="M5 5H9M5 7H9M5 9H9" stroke="#fff" stroke-width=".7"/></svg><h4>Lorem Ipsum</h4><p>Lorem Ipsum has been the dummy text and can be replaced with your original text here.</p></div>
    <p class="foot">Presentation Title goes here | www.norvaleworks.se</p>
    <span class="page-no">05</span>
  </section>

  <section class="slide col-3 row-4">
    <span class="title-dot"></span>
    <h2 class="slide-title">Statistic Bar</h2>
    <div class="brand sm">Norvale<br>Works</div>
    <svg class="el" style="left:6px;top:46px;width:150px;height:112px" viewBox="0 0 150 112" role="img" aria-label="Grouped bar chart for 2015 to 2018">
      <g font-size="3.6" fill="#555" text-anchor="end">
        <text x="12" y="10">250</text><text x="12" y="27">200</text><text x="12" y="44">150</text><text x="12" y="61">100</text><text x="12" y="78">50</text><text x="12" y="95">0</text>
      </g>
      <path d="M15 8V94H146" stroke="#999" stroke-width=".4" fill="none"/>
      <g fill="#a9cdf0">
        <rect x="19" y="25" width="6" height="69"/><rect x="36" y="41" width="6" height="53"/><rect x="53" y="33" width="6" height="61"/><rect x="70" y="48" width="6" height="46"/>
        <rect x="87" y="38" width="6" height="56"/><rect x="104" y="44" width="6" height="50"/><rect x="121" y="22" width="6" height="72"/>
      </g>
      <g fill="var(--blue)">
        <rect x="26" y="40" width="6" height="54"/><rect x="43" y="56" width="6" height="38"/><rect x="60" y="45" width="6" height="49"/><rect x="77" y="62" width="6" height="32"/>
        <rect x="94" y="52" width="6" height="42"/><rect x="111" y="64" width="6" height="30"/><rect x="128" y="35" width="6" height="59"/>
      </g>
      <g font-size="3.6" fill="#555" text-anchor="middle">
        <text x="30" y="101">2015</text><text x="63" y="101">2016</text><text x="97" y="101">2017</text><text x="131" y="101">2018</text>
      </g>
    </svg>
    <div class="stat-note"><b>Put your highlight here as main statement of the diagram</b>
      <ul><li>Neque porro quisquam est, qui dolorem ipsum quia dolor sit amet, consectetur.</li><li>At vero eos et accusamus et iusto odio dignissimos ducimus qui blanditiis praesentium voluptatum.</li><li>Neque porro quisquam est, qui dolorem ipsum quia dolor sit amet, consectetur.</li><li>At vero eos et accusamus et iusto odio dignissimos ducimus qui blanditiis praesentium voluptatum.</li></ul></div>
    <div class="art" role="img" aria-label="Illustration of a man presenting a chart on a screen" style="left:246px;top:44px;width:46px;height:130px;border-radius:16px"></div>
    <p class="foot">Presentation Title goes here | www.norvaleworks.se</p>
    <span class="page-no">06</span>
  </section>

  <!-- Row 5 -->
  <section class="slide col-1 row-5">
    <svg class="shape" viewBox="0 0 293 184" aria-hidden="true"><path d="M20 10C80 -4 160 6 230 16C280 24 296 70 280 120C266 166 220 184 150 184C80 184 30 176 14 140C0 100 -4 20 20 10Z" fill="var(--pale)"/></svg>
    <span class="title-dot"></span>
    <h2 class="slide-title">Timeline</h2>
    <div class="brand sm">Norvale<br>Works</div>
    <div class="tl-entry" style="left:37px;top:40px"><b>2012</b>Nemo enim ipsam voluptatem quia voluptas sit aspernatur aut odit aut fugit, sed quia consequuntur magni dolores.</div>
    <div class="tl-entry" style="left:107px;top:40px"><b>2014</b>Nemo enim ipsam voluptatem quia voluptas sit aspernatur aut odit aut fugit, sed quia consequuntur magni dolores.</div>
    <div class="tl-entry" style="left:177px;top:40px"><b>2016</b>Nemo enim ipsam voluptatem quia voluptas sit aspernatur aut odit aut fugit, sed quia consequuntur magni dolores.</div>
    <svg class="el" style="left:0;top:0;width:293px;height:184px" viewBox="0 0 293 184" aria-hidden="true">
      <g fill="#fff" stroke="#6d9cec" stroke-width=".9">
        <polygon points="48,92 62,100 62,116 48,124 34,116 34,100"/>
        <polygon points="91,92 105,100 105,116 91,124 77,116 77,100"/>
        <polygon points="134,92 148,100 148,116 134,124 120,116 120,100"/>
        <polygon points="183,92 197,100 197,116 183,124 169,116 169,100"/>
        <polygon points="226,92 240,100 240,116 226,124 212,116 212,100"/>
      </g>
      <g fill="none" stroke="#6d9cec" stroke-width=".7">
        <circle cx="48" cy="108" r="4"/><path d="M87 104L95 112M95 104L87 112"/><path d="M129 112L133 107L136 110L140 104"/><path d="M178 110L183 105L188 110"/><rect x="222" y="103" width="8" height="10"/>
      </g>
    </svg>
    <div class="tl-entry" style="left:78px;top:130px"><b>2013</b>Nemo enim ipsam voluptatem quia voluptas sit aspernatur aut odit aut fugit, sed quia consequuntur magni dolores.</div>
    <div class="tl-entry" style="left:157px;top:130px"><b>2017</b>Nemo enim ipsam voluptatem quia voluptas sit aspernatur aut odit aut fugit, sed quia consequuntur magni dolores.</div>
    <p class="foot">Presentation Title goes here | www.norvaleworks.se</p>
    <span class="page-no">07</span>
  </section>

  <section class="slide col-2 row-5">
    <h2 class="slide-title" style="left:19px">Testimonial</h2>
    <div class="brand sm">Norvale<br>Works</div>
    <div class="quote-box" style="left:24px;top:48px">“ Maecenas sed diam eget risus varius blandit sit amet non magna. Donec id elit non mi porta gravida at eget metus. Maecenas sed risus. ”</div>
    <div class="quote-frame" style="left:111px;top:48px"></div>
    <div class="quote-name" style="left:28px;top:87px">Mara Lindqvist<span>CEO Harbourline</span></div>
    <div class="quote-box" style="left:158px;top:48px">“ Maecenas sed diam eget risus varius blandit sit amet non magna. Donec id elit non mi porta gravida at eget metus. Maecenas sed risus. ”</div>
    <div class="quote-frame" style="left:245px;top:48px"></div>
    <div class="quote-name" style="left:164px;top:87px">Jonas Ekholm<span>CEO Fieldpoint</span></div>
    <div class="quote-box" style="left:24px;top:104px">“ Maecenas sed diam eget risus varius blandit sit amet non magna. Donec id elit non mi porta gravida at eget metus. Maecenas sed risus. ”</div>
    <div class="quote-frame" style="left:111px;top:104px"></div>
    <div class="quote-name" style="left:28px;top:143px">Mara Lindqvist<span>CEO Harbourline</span></div>
    <div class="quote-box" style="left:158px;top:104px">“ Maecenas sed diam eget risus varius blandit sit amet non magna. Donec id elit non mi porta gravida at eget metus. Maecenas sed risus. ”</div>
    <div class="quote-frame" style="left:245px;top:104px"></div>
    <div class="quote-name" style="left:164px;top:143px">Petra Sandell<span>CEO Ostvik</span></div>
    <p class="foot">Presentation Title goes here | www.norvaleworks.se</p>
    <span class="page-no">08</span>
  </section>

  <section class="slide col-3 row-5">
    <svg class="shape" viewBox="0 0 293 184" aria-hidden="true"><path d="M0 0H30C40 12 30 24 14 24C6 24 2 20 0 18Z" fill="var(--pale)"/><path d="M293 130C270 136 250 160 262 184H293Z" fill="var(--blue-soft)"/><path d="M250 184C256 170 276 168 293 176V184Z" fill="var(--blue)"/></svg>
    <div class="art" role="img" aria-label="Illustration of a doctor and a woman shaking hands over a tablet" style="left:18px;top:26px;width:132px;height:130px;border-radius:50%"></div>
    <div class="brand lg" style="left:221px;top:20px;font-size:9px">Norvale<br>Works</div>
    <p class="thanks" style="left:156px;top:71px">thank you</p>
    <p class="contact" style="left:157px;top:95px">Lorem Ipsum 12<br>55210 Lindvik<br>Country X<br>T&nbsp;&nbsp;0612 555 0148<br>F&nbsp;&nbsp;0612 555 0149<br>E&nbsp;&nbsp;hello@norvaleworks.se<br>www.norvaleworks.se</p>
    <p class="follow" style="left:23px;top:159px">Norvale Works</p>
  </section>

  <!-- Row 6 -->
  <section class="slide col-1 row-6">
    <span class="title-dot"></span>
    <h2 class="slide-title">Disclaimer</h2>
    <div class="brand sm">Norvale<br>Works</div>
    <div class="legal">
      <p>This presentation has been prepared on a confidential basis solely for your benefit and is provided only on request. This presentation and any information contained herein is not to be reproduced or redistributed. By accepting and viewing this presentation, you agree to keep all information contained herein strictly confidential and not to disclose the same to anyone other than your officers, employees and professional advisors on a confidential basis.</p>
      <p>This presentation is not an offer to sell or a solicitation of an offer to buy any securities, nor shall any securities be offered or sold to any person in any jurisdiction in which such an offer, solicitation, purchase or sale would be unlawful. Any offer of interests in the fund will be made only upon delivery of the confidential offering memorandum of the fund.</p>
      <p>The information contained herein has been compiled as of February 1, 2019 unless otherwise stated herein, and is qualified in its entirety by reference to the confidential offering memorandum and the limited partnership agreement of the fund. No obligation is undertaken to update such information, whether as a result of new information, further events, or otherwise.</p>
      <p>The performance data presented herein is gross of performance fees, management fees and other fees and expenses unless otherwise stated herein. Projected performance data shown for unrealized investments constitutes forward-looking statements. The forward-looking data is based on numerous assumptions and is speculative in nature. Actual results may vary significantly from the values and rates of return projected for such investments. Past performance is not necessarily indicative of future results, and there can be no assurance that the fund will achieve comparable results or that targeted returns will be met.</p>
    </div>
    <p class="foot">Presentation Title goes here | www.norvaleworks.se</p>
    <span class="page-no">09</span>
  </section>

  <section class="slide col-2 row-6 is-blue">
    <svg class="shape" viewBox="0 0 293 184" aria-hidden="true"><path d="M20 20C70 0 140 10 170 40C196 66 180 110 150 140C120 170 60 176 30 150C4 126 -10 36 20 20Z" fill="var(--blue-mid)"/><path d="M293 0V60C270 50 250 30 262 0Z" fill="var(--blue-mid)"/></svg>
    <div class="art on-blue" role="img" aria-label="Illustration of a man inside a large phone surrounded by social media icons" style="left:150px;top:22px;width:128px;height:140px;border-radius:40%"></div>
    <div class="brand lg white" style="left:31px;top:38px;font-size:9px">Norvale<br>Works</div>
    <p class="thanks" style="left:30px;top:78px">thank you</p>
    <p class="contact" style="left:31px;top:99px">Lorem Ipsum 12<br>55210 Lindvik<br>Country X</p>
    <p class="contact" style="left:31px;top:127px">T&nbsp;&nbsp;0612 555 0148<br>F&nbsp;&nbsp;0612 555 0149</p>
    <p class="contact" style="left:90px;top:127px">E&nbsp;&nbsp;hello@norvaleworks.se<br>&nbsp;&nbsp;&nbsp;&nbsp;www.norvaleworks.se</p>
    <p class="follow" style="left:236px;top:168px">Norvale Works</p>
  </section>

  <section class="slide col-3 row-6">
    <svg class="shape" viewBox="0 0 293 184" aria-hidden="true"><path d="M40 50C90 30 170 40 210 60C250 80 240 140 200 160C150 184 70 180 46 150C24 122 0 66 40 50Z" fill="var(--pale)"/><path d="M200 60C230 30 280 40 290 80C298 120 270 160 230 160C200 160 180 130 186 100C190 80 194 66 200 60Z" fill="var(--pale-2)"/></svg>
    <h2 class="slide-title">Quote</h2>
    <div class="brand sm">Norvale<br>Works</div>
    <p class="quote-text">A well run architecture function is as important as a flight tower at an airport. We must secure timely and purposeful use of technology to boost business ambitions</p>
    <p class="quote-author">Henrik Falk</p>
    <div class="photo" role="img" aria-label="Portrait photo of a smiling man in a dark suit" style="left:190px;top:42px;width:82px;height:118px;border-radius:40% 40% 30% 30%;background:linear-gradient(160deg,#7c8aa0,#26324a)"></div>
    <p class="foot">Presentation Title goes here | www.norvaleworks.se</p>
    <span class="page-no">10</span>
  </section>

</main>
</body>
</html>
```